Website Design for Quarnel Records, LLC a record label

We're in the business of promoting music and music videos, and the artists who make them. We are based in New York City. This is a website design for a record label. At first we will concentrate on Hip-Hop music, but in the future we may decide to do othe

```html
<!DOCTYPE html>
<html lang="en">
<head>
<meta charset="utf-8">
<title>Quarnel Records</title>
<link href="https://fonts.googleapis.com/css2?family=Questrial&family=Arimo:ital,wght@0,400;0,700;1,400&display=swap" rel="stylesheet">
<style>
:root{
  --black:#050505;
  --panel:#1c1c1e;
  --panel-dark:#111113;
  --band:#232325;
  --red:#d8182a;
  --red-dark:#6a0a12;
  --white:#ffffff;
  --grey:#b9b9b9;
  --muted:#8a8a8a;
}
*{margin:0;padding:0;box-sizing:border-box}
html,body{width:1200px;height:593px;overflow:hidden;background:var(--black)}
body{font-family:"Arimo",Arial,sans-serif;color:var(--white);position:relative;
  background:radial-gradient(ellipse at 50% 30%,#1a1a1a 0%,#0a0a0a 55%,#030303 100%)}
.abs{position:absolute}
.header-band{left:187px;top:40px;width:840px;height:200px;
  background:linear-gradient(180deg,#2a2a2c 0%,#1e1e20 60%,#141415 100%)}
.brand{left:200px;top:48px;font-family:"Questrial",sans-serif;font-size:30px;letter-spacing:2px;color:var(--white)}
.brand-dot{left:420px;top:122px;width:120px;height:120px;border-radius:50%;background:var(--red)}
.social{left:793px;top:42px;display:flex;gap:11px}
.social span{width:29px;height:33px;border-radius:6px;background:linear-gradient(180deg,#e5303c,#8d0c16);border:1px solid #f05a63}
.artists-title{left:187px;top:97px;font-family:"Questrial",sans-serif;font-size:16px;color:var(--red)}
.artist-list{left:219px;top:120px;display:grid;grid-template-columns:62px 63px 60px;row-gap:9px;font-size:11px;color:var(--grey)}
.artist-list .more{font-weight:700;color:var(--white)}
.newsletter-title{left:929px;top:102px;font-family:"Questrial",sans-serif;font-size:17px;letter-spacing:1px}
.newsletter-form{left:873px;top:124px;display:flex;gap:4px}
.newsletter-form .field{width:87px;height:12px;border:1px solid #555;background:#111;font-size:6px;color:var(--muted);padding-left:3px;line-height:10px}
.newsletter-form .btn{width:57px;height:12px;border:1px solid #888;background:#0d0d0d;font-size:7px;text-align:center;line-height:10px}
.nav-band{left:613px;top:158px;width:414px;height:58px;
  background:linear-gradient(90deg,rgba(120,10,20,0) 0%,var(--red-dark) 25%,#8e0f1b 70%,#5e0810 100%)}
.nav{font-family:"Questrial",sans-serif;font-size:17px;letter-spacing:.5px}
.panel{background:linear-gradient(180deg,var(--panel),var(--panel-dark));border-left:4px solid var(--red)}
.player{left:219px;top:267px;width:204px;height:77px}
.player .now{background:linear-gradient(90deg,#7a0b14,#2a0a0c);height:16px;font-size:9px;font-style:italic;padding:2px 8px}
.player .ctrl{display:flex;justify-content:space-between;font-size:8px;font-style:italic;padding:3px 6px;color:#ddd}
.player .track{font-size:9px;color:#ddd;padding:1px 14px;margin:1px 4px;background:#2a2a2c}
.gallery{left:219px;top:367px;width:204px;height:113px}
.gallery h3{font-size:10px;font-weight:400;padding:6px 10px}
.thumbs{display:grid;grid-template-columns:repeat(3,44px);column-gap:16px;row-gap:8px;padding:0 12px}
.thumbs div{height:32px}
.gallery .more-at{position:absolute;right:28px;bottom:10px;font-size:8px;font-style:italic}
.gallery .go{position:absolute;right:6px;bottom:5px;width:20px;height:17px;border-radius:4px;background:var(--red)}
.feature{left:456px;top:220px;width:404px;height:300px;background:linear-gradient(180deg,#1b1b1c,#0e0e0f);border:2px solid #6a0b13}
.feature-photo{left:6px;top:11px;width:392px;height:206px;background:radial-gradient(ellipse at 35% 30%,#e7c8f4 0%,#a04ab8 25%,#4a1470 55%,#1a0826 100%)}
.latest{right:4px;top:4px;width:72px;height:26px;background:rgba(0,0,0,.55);font-family:"Questrial",sans-serif;font-size:16px;text-align:center;line-height:26px}
.feature h2{left:28px;top:222px;font-family:"Questrial",sans-serif;font-weight:400;font-size:13px}
.feature .date{right:40px;top:225px;font-size:8px;color:#ddd}
.feature p{left:28px;font-size:8px;line-height:10px;color:#ddd}
.side{left:867px;width:142px;height:67px;border:2px solid #5a0a12}
.side .img{position:absolute;inset:0}
.side .cap{position:absolute;right:8px;bottom:13px;font-size:6px}
.side .det{position:absolute;right:8px;bottom:3px;font-size:6px;color:#ccc}
.footer{left:247px;top:569px;font-size:7px;color:var(--muted)}
</style>
</head>
<body>
  <div class="abs header-band"></div>
  <div class="abs brand-dot"></div>
  <div class="abs brand">QUARNEL RECORDS</div>

  <div class="abs social" aria-label="Social links">
    <span></span><span></span><span></span><span></span><span></span><span></span>
  </div>

  <div class="abs artists-title">ARTISTS</div>
  <div class="abs artist-list">
    <span>artist1</span><span>artist6</span><span>artist11</span>
    <span>artist2</span><span>artist7</span><span>artist12</span>
    <span>artist3</span><span>artist8</span><span>artist13</span>
    <span>artist4</span><span>artist9</span><span>artist14</span>
    <span>artist5</span><span>artist10</span><span class="more">more&#9656;</span>
  </div>

  <div class="abs newsletter-title">NEWSLETTER</div>
  <div class="abs newsletter-form"><div class="field">Your E-mail Address</div><div class="btn">SUBSCRIBE</div></div>

  <div class="abs nav-band"></div>
  <nav class="nav">
    <span class="abs" style="left:640px;top:163px">NEWS</span>
    <span class="abs" style="left:708px;top:163px">ARTISTS</span>
    <span class="abs" style="left:797px;top:163px">MUSIC</span>
    <span class="abs" style="left:873px;top:163px">VIDEO</span>
    <span class="abs" style="left:940px;top:163px">GALLERY</span>
    <span class="abs" style="left:640px;top:187px">SCHEDULE</span>
    <span class="abs" style="left:744px;top:187px">SHOP</span>
    <span class="abs" style="left:819px;top:187px">ABOUT US</span>
    <span class="abs" style="left:932px;top:187px">CONTACT</span>
  </nav>

  <section class="abs panel player">
    <div class="now">Now Playing ~ Songname | Artist</div>
    <div class="ctrl"><span style="color:var(--red);font-style:normal">&#9654; &#10074;&#10074; &#9679;</span><span>Get Ringtones&#9656;</span></div>
    <div class="track">Songname | Artist1 | Singlename</div>
    <div class="track">Songname | Artist6 | Albumname</div>
    <div class="track">Songname | Artist3 | Singlename</div>
  </section>

  <section class="abs panel gallery">
    <h3>GALLERY</h3>
    <div class="thumbs">
      <div role="img" aria-label="Gallery photo: stage crowd" style="background:linear-gradient(135deg,#555,#111)"></div>
      <div role="img" aria-label="Gallery photo: spotlight" style="background:linear-gradient(135deg,#9aa,#222)"></div>
      <div role="img" aria-label="Gallery photo: blue concert" style="background:linear-gradient(135deg,#3b7fb0,#0b1a30)"></div>
      <div role="img" aria-label="Gallery photo: dark stage" style="background:linear-gradient(135deg,#333,#050505)"></div>
      <div role="img" aria-label="Gallery photo: blue lights" style="background:linear-gradient(135deg,#2a5fd0,#0a0f30)"></div>
      <div role="img" aria-label="Gallery photo: colour lights" style="background:linear-gradient(135deg,#4ca060,#6a2a90)"></div>
    </div>
    <span class="more-at">More at</span><span class="go"></span>
  </section>

  <section class="abs feature">
    <div class="abs feature-photo" role="img" aria-label="Concert photo: performer on stage under purple lights">
      <div class="abs latest">LATEST</div>
    </div>
    <h2 class="abs">ARTIST9 FIRST LIVE</h2>
    <span class="abs date">Posted: 20/01/2012</span>
    <p class="abs" style="top:242px">Artist9's first live will be held at the XYZ on the 13th of the Febuaury, don't miss it!<br>Tickets may be purchased <u>here.</u></p>
    <p class="abs" style="top:269px">Artist9 is an upcoming... &nbsp;<b><u>Read More</u></b></p>
  </section>

  <div class="abs side" style="top:220px"><div class="img" role="img" aria-label="Vinyl record photo" style="background:radial-gradient(circle at 40% 50%,#7ad 0%,#335 40%,#111 80%)"></div><span class="cap">ARTIST4 NEW SINGLE</span><span class="det">Details</span></div>
  <div class="abs side" style="top:291px"><div class="img" role="img" aria-label="Live performance photo" style="background:radial-gradient(circle at 40% 40%,#e6c0f0 0%,#9040b0 35%,#200a30 90%)"></div><span class="cap">ARTIST9 FIRST LIVE</span><span class="det">Details</span></div>
  <div class="abs side" style="top:362px"><div class="img" role="img" aria-label="Club crowd photo" style="background:linear-gradient(160deg,#c04070 0%,#502040 50%,#100510 100%)"></div><span class="cap">ARTIST13 DEBUT</span><span class="det">Details</span></div>
  <div class="abs side" style="top:433px"><div class="img" role="img" aria-label="DJ booth photo" style="background:linear-gradient(160deg,#4060d0 0%,#a03070 50%,#100510 100%)"></div><span class="cap">CHECK OUT CLUB 123 FOR ARTIST1</span><span class="det">Details</span></div>

  <footer class="abs footer">(C) QUARNEL RECORDS &nbsp;| &nbsp;Terms of Use &nbsp;| &nbsp;Privacy Policy &nbsp;|</footer>
</body>
</html>
```